Letterhead Design Project

Need Letterhead and Envelpe design with One Single or Both Side pockets for a yong dynamic employee friendly IT services company. It should be professional and sleek and should look fresh.

Target Market(s)

IT Corporate

Industry/Entity Type

It Company

```html
<!DOCTYPE html>
<html lang="en">
<head>
<meta charset="utf-8">
<title>Kavrin – Letterhead and Envelope</title>
<link rel="stylesheet" href="https://fonts.googleapis.com/css2?family=Roboto+Condensed:wght@300;400;700&family=Open+Sans:wght@400&display=swap">
<style>
  :root{
    --bg-light:#f4f4f5;
    --bg-dark:#dedfe1;
    --paper:#ffffff;
    --orange:#f08a2c;
    --orange-deep:#ec6f28;
    --orange-light:#f6a53a;
    --brand:#b8741c;
    --ink:#2f2f2f;
    --body:#8a8a8a;
    --window:#ebecec;
  }
  *{margin:0;padding:0;box-sizing:border-box}
  html,body{width:1200px;height:1200px;overflow:hidden}
  body{
    position:relative;
    background:radial-gradient(circle at 50% 50%,var(--bg-light) 0%,var(--bg-dark) 100%);
    font-family:"Open Sans",sans-serif;
  }
  .envelope{position:absolute;left:55px;top:457px;width:480px;height:292px}
  .envelope__flap{
    position:absolute;left:0;top:0;width:480px;height:52px;
    background:linear-gradient(180deg,var(--orange-deep),var(--orange-light));
    clip-path:polygon(2% 0,98% 0,100% 100%,0 100%);
    border-radius:6px 6px 0 0;
  }
  .envelope__body{position:absolute;left:0;top:52px;width:480px;height:240px;background:var(--paper);overflow:hidden}
  .brand{
    position:absolute;font-family:"Roboto Condensed",sans-serif;font-weight:700;
    color:var(--brand);letter-spacing:1px;line-height:1;
  }
  .envelope .brand{left:26px;top:31px;font-size:30px}
  .contact{
    position:absolute;left:252px;top:51px;
    font-family:"Roboto Condensed",sans-serif;font-size:11px;line-height:16px;color:var(--ink);
  }
  .address-window{position:absolute;left:237px;top:127px;width:208px;height:77px;background:var(--window);border-radius:6px}
  .pixel-band{position:absolute;background:linear-gradient(90deg,var(--orange-deep),var(--orange) 55%,rgba(246,165,58,0.15))}
  .envelope .pixel-band{left:0;top:176px;width:226px;height:64px}
  .swoosh{position:absolute;left:0;pointer-events:none}
  .letterhead{position:absolute;left:649px;top:253px;width:458px;height:648px;background:var(--paper);overflow:hidden}
  .letterhead__title{
    position:absolute;left:79px;top:48px;font-family:"Roboto Condensed",sans-serif;
    font-weight:700;font-size:27px;color:var(--ink);letter-spacing:-0.3px;
  }
  .letterhead .brand{right:32px;top:44px;font-size:30px}
  .letterhead__heading{
    position:absolute;left:79px;top:155px;font-family:"Roboto Condensed",sans-serif;
    font-weight:300;font-size:21px;color:var(--orange);
  }
  .letterhead__body{position:absolute;left:79px;top:214px;width:330px}
  .letterhead__body p{font-size:8.6px;line-height:12px;color:var(--body);margin-bottom:12px}
  .letterhead .pixel-band{left:0;top:560px;width:307px;height:88px}
</style>
</head>
<body>
  <section class="envelope">
    <div class="envelope__flap"></div>
    <div class="envelope__body">
      <div class="brand">kavrin</div>
      <div class="contact">
        Phone: + 1 234 56789<br>
        Adress: Your City. Your adress.<br>
        Mail: mail@example.com
      </div>
      <div class="address-window"></div>
      <svg class="swoosh" width="480" height="240" style="top:0">
        <path d="M0 146 C60 138 110 160 150 200 S200 240 210 240" fill="none" stroke="#f3c9a3" stroke-width="0.8"/>
      </svg>
      <div class="pixel-band" role="img" aria-label="Orange pixel-square motif"></div>
    </div>
  </section>

  <section class="letterhead">
    <h1 class="letterhead__title">SAMPLE TEXT</h1>
    <div class="brand">kavrin</div>
    <h2 class="letterhead__heading">Lorem ipsum dolor sit amet</h2>
    <div class="letterhead__body">
      <p>Lorem ipsum dolor sit amet, consectetuer adipiscing elit, sed diam nonummy nibh euismod tincidunt ut laoreet dolore magna aliquam erat volutpat. Ut wisi enim ad minim veniam, quis nostrud exerci tation ullamcorper suscipit lobortis nisl ut aliquip ex ea commodo consequat. Duis autem vel eum iriure dolor in hendrerit in vulputate velit esse molestie consequat, vel illum dolore eu feugiat nulla facilisis at vero eros et accumsan et iusto odio dignissim qui blandit praesent luptatum zzril delenit augue duis dolore te feugait nulla facilisi.</p>
      <p>Lorem ipsum dolor sit amet, consectetuer adipiscing elit, sed diam nonummy nibh euismod tincidunt ut laoreet dolore magna aliquam erat volutpat. Ut wisi enim ad minim veniam, quis nostrud exerci tation ullamcorper suscipit lobortis nisl ut aliquip ex ea commodo consequat. Duis autem vel eum iriure dolor in hendrerit in vulputate velit esse molestie consequat, vel illum dolore eu feugiat nulla facilisis at vero eros et accumsan et iusto odio dignissim qui blandit praesent luptatum zzril delenit augue duis dolore te feugait nulla facilisi.</p>
      <p>Lorem ipsum dolor sit amet, consectetuer adipiscing elit, sed diam nonummy nibh euismod tincidunt ut laoreet dolore magna aliquam erat volutpat. Ut wisi enim ad minim veniam, quis nostrud exerci tation ullamcorper suscipit lobortis nisl ut aliquip ex ea commodo consequat. Duis autem vel eum iriure dolor in hendrerit in vulputate velit esse molestie consequat, vel illum dolore eu feugiat nulla facilisis at vero eros et accumsan et iusto odio dignissim qui blandit praesent luptatum zzril delenit augue duis dolore te feugait nulla facilisi.</p>
    </div>
    <svg class="swoosh" width="458" height="648" style="top:0">
      <path d="M0 520 C90 508 160 540 210 600 S250 648 260 648" fill="none" stroke="#f3c9a3" stroke-width="0.8"/>
    </svg>
    <div class="pixel-band" role="img" aria-label="Orange pixel-square motif"></div>
  </section>
</body>
</html>
```